Design our branded business card!

We'd love for you to design our business card and come up with a fitting design that reflects the Brimble brand. We're a growing tech startup with big ambitions. We've included our brand guidelines (contain colour palette), logo (EPS vector in CMYK) and old designs to help you on your way.

We'd like to keep the design fairly simple:

* Name
* Phone number
* Email address
* Website (www.brimble.life)
* Twitter (@brimble)
* Address (19 Fenwick Row, Leeds, UK, LS4 9QT).

This would need to include print and cutting marks.

If you have any questions just let us know!

Target Market(s)

Businesses, Press and our customers!

Industry/Entity Type

Business

Contact Information for Business Card

* Name
* Phone number
* Email address
* Twitter (@brimble)

Font styles to use
Sans Serif

Requirements
Must have
• 1. Must have the Brimble logo included.
• 2. Must use the font 'Brandon Text' in either 'light' or 'thin' (https://www.typevaultex.com/fonts/qrnfoundry/brandon-text/)
• 3. Must use exact colours references from the brand guidelines. Colours outside of the brand guidelines will be discounted. White (transparent) backgrounds are fine.
• 4. Must contain the following information:
• * Name
• * Phone number
• * Email address
• * Website (www.brimble.life)
• * Twitter (@brimble)
• * Address (19 Fenwick Row, Leeds, UK, LS4 9QT).
Nice to have
• Must use the font 'Brandon Text' in either 'light' or 'thin' (https://www.typevaultex.com/fonts/qrnfoundry/brandon-text/)
Should not have
• Colours outside of the brand guidelines will be discounted. White (transparent) backgrounds are fine.
• Avoid creating icons or including photography.

```html
<!DOCTYPE html>
<html lang="en">
<head>
<meta charset="utf-8">
<title>Brimble Business Card</title>
<link rel="stylesheet" href="https://fonts.googleapis.com/css2?family=Mulish:wght@300;400&display=swap">
<style>
  :root {
    --backdrop: #2f3f48;
    --brand-green: #7cbf6e;
    --paper: #ffffff;
    --ink: #333a3d;
    --ink-soft: #3d4447;
  }
  html, body {
    margin: 0;
    width: 1200px;
    height: 900px;
    overflow: hidden;
    background: var(--backdrop);
    font-family: "Mulish", sans-serif;
    font-weight: 300;
  }
  .card {
    position: absolute;
    left: 300px;
    width: 600px;
    height: 388px;
    overflow: hidden;
  }
  .card-front { top: 50px; background: var(--brand-green); }
  .card-back  { top: 462px; background: var(--paper); }

  .brand-lockup {
    position: absolute;
    display: flex;
    align-items: center;
    gap: 22px;
  }
  .brand-mark {
    width: 92px;
    height: 92px;
    border-radius: 50%;
  }
  .brand-name {
    font-size: 64px;
    font-weight: 300;
    letter-spacing: 1px;
    line-height: 1;
  }
  .card-front .brand-lockup { left: 105px; top: 98px; }
  .card-front .brand-mark { background: var(--paper); }
  .card-front .brand-name { color: var(--paper); }

  .web-strip {
    position: absolute;
    left: 8px;
    right: 8px;
    top: 282px;
    height: 34px;
    background: var(--paper);
    color: var(--ink);
    font-size: 19px;
    letter-spacing: 9px;
    text-align: center;
    line-height: 34px;
  }

  .card-back .brand-lockup { left: 222px; top: 26px; }
  .card-back .brand-mark { background: var(--brand-green); }
  .card-back .brand-name { color: var(--ink); }

  .holder-name {
    position: absolute;
    left: 36px;
    top: 202px;
    margin: 0;
    font-size: 27px;
    font-weight: 300;
    color: var(--ink);
  }
  .holder-address {
    position: absolute;
    left: 36px;
    top: 242px;
    margin: 0;
    font-size: 15px;
    color: var(--ink-soft);
    letter-spacing: 0.3px;
  }

  .contact-band {
    position: absolute;
    left: 8px;
    right: 8px;
    height: 30px;
    background: var(--brand-green);
    color: var(--paper);
    font-size: 16px;
    letter-spacing: 0.5px;
  }
  .contact-band.upper { top: 296px; }
  .contact-band.lower { top: 336px; }
  .contact-item {
    position: absolute;
    top: 0;
    height: 30px;
    display: flex;
    align-items: center;
    gap: 14px;
  }
  .contact-item.left { left: 28px; }
  .contact-item.right { left: 374px; }
  .contact-icon { width: 26px; height: 22px; }
  .social-dot {
    width: 18px;
    height: 18px;
    border-radius: 50%;
    background: var(--paper);
    margin: 0 4px;
  }
</style>
</head>
<body>

<section class="card card-front" aria-label="Card front">
  <div class="brand-lockup">
    <span class="brand-mark"></span>
    <span class="brand-name">brimble</span>
  </div>
  <div class="web-strip">www.brimble.life</div>
</section>

<section class="card card-back" aria-label="Card back">
  <div class="brand-lockup">
    <span class="brand-mark"></span>
    <span class="brand-name">brimble</span>
  </div>

  <h1 class="holder-name">Name</h1>
  <p class="holder-address">19 Fenwick Row, Leeds, UK, LS4 9QT</p>

  <div class="contact-band upper">
    <div class="contact-item left">
      <svg class="contact-icon" viewBox="0 0 26 22" aria-hidden="true">
        <path d="M2 7 Q13 0 24 7 L21 10 L18 8 L18 6 Q13 4 8 6 L8 8 L5 10 Z" fill="#fff"/>
        <path d="M7 10 L19 10 L22 20 L4 20 Z" fill="#fff"/>
        <circle cx="13" cy="15" r="3" fill="none" stroke="#7cbf6e" stroke-width="1.4"/>
      </svg>
      <span>111-1111-1111</span>
    </div>
    <div class="contact-item right">
      <span class="social-dot"></span>
      <span>@brimble</span>
    </div>
  </div>

  <div class="contact-band lower">
    <div class="contact-item left">
      <svg class="contact-icon" viewBox="0 0 26 22" aria-hidden="true">
        <rect x="1.5" y="2.5" width="23" height="17" fill="none" stroke="#fff" stroke-width="1.6"/>
        <path d="M1.5 2.5 L13 12 L24.5 2.5 M1.5 19.5 L10 10 M24.5 19.5 L16 10" fill="none" stroke="#fff" stroke-width="1.6"/>
      </svg>
      <span>email@email.com</span>
    </div>
    <div class="contact-item right">
      <svg class="contact-icon" viewBox="0 0 26 22" aria-hidden="true">
        <g fill="none" stroke="#fff" stroke-width="1.4">
          <circle cx="13" cy="11" r="9.5"/>
          <ellipse cx="13" cy="11" rx="4.5" ry="9.5"/>
          <path d="M3.5 11 H22.5 M5 6 H21 M5 16 H21 M13 1.5 V20.5"/>
        </g>
      </svg>
      <span>www.brimble.life</span>
    </div>
  </div>
</section>

</body>
</html>
```